Website for Foodstuff Import-Export Company *

We need a website for our company which imports and sell ( edible oil , ketchup , mayonnaise and pulses ). our current website is brevonix.pl , we need a website which has corporate appearance with good quality products.

Target Market(s)

European Wholesalers , Supermarket Chains,

Coding

Coded - Design and coding required

Number of Pages Required

1 page

```html
<!DOCTYPE html>
<html lang="en">
<head>
<meta charset="utf-8">
<title>Brevonix – About us</title>
<link href="https://fonts.googleapis.com/css2?family=Playfair+Display:wght@400;700&family=Montserrat:wght@300;400;500&display=swap" rel="stylesheet">
<style>
:root{
  --yellow:#f6c800;
  --gold:#e3a51c;
  --ink:#555a5e;
  --muted:#7d7f82;
  --cream:#f7f5ef;
  --card:#f1efea;
  --footer:#3e4149;
  --white:#fff;
  --green:#4aa54a;
}
*{margin:0;padding:0;box-sizing:border-box}
html,body{width:1200px;height:3397px;overflow:hidden;background:var(--white)}
body{position:relative;font-family:"Montserrat",sans-serif;color:var(--ink)}
.abs{position:absolute}
.serif{font-family:"Playfair Display",serif;font-weight:700}
.center{text-align:center}

/* header */
.site-header{left:0;top:0;width:1200px;height:69px;background:var(--white)}
.brand{left:160px;top:22px;font-size:20px;font-weight:500;color:var(--green);letter-spacing:1px}
.nav{left:345px;top:29px;display:flex;gap:40px;font-size:11px;letter-spacing:1px;color:#555;list-style:none}
.nav li:first-child{color:var(--gold)}

/* hero */
.hero{left:0;top:69px;width:1200px;height:350px;background:linear-gradient(100deg,#55534f 0%,#65625c 45%,#6e6343 70%,#8a7628 85%,#3e3a2e 100%)}
.hero-title{left:0;top:165px;width:1200px;font-size:58px;color:#f0ece2}
.crumbs{left:0;top:260px;width:1200px;font-size:19px;color:#f0ece2}
.crumbs span{margin:0 12px;font-weight:400;opacity:.7}

.badge{width:74px;height:74px;border-radius:50%;background:var(--white)}
.badge i{position:absolute;left:22px;top:26px;width:30px;height:16px;border-radius:50%;background:linear-gradient(90deg,#5f8f2a,#c9c23a)}

.section-title{left:0;width:1200px;font-size:34px;color:#4f5358}

/* story */
.story-box{left:161px;top:624px;width:878px;height:337px;border:2px solid var(--yellow)}
.story-photo{left:191px;top:659px;width:303px;height:271px;background:radial-gradient(ellipse at 45% 50%,#f0c22a 0%,#e9b21b 30%,#f7f3e8 60%,#fff 80%)}
.story-card{left:720px;top:674px;width:273px;height:154px;background:var(--card)}
.story-card h3{height:49px;line-height:49px;background:var(--yellow);color:#6b5a1a;font-size:18px}
.story-card p{padding:26px 16px 0;font-size:9.5px;line-height:16px;color:#777}
.card-tip{left:848px;top:827px;width:0;height:0;border-left:9px solid transparent;border-right:9px solid transparent;border-top:10px solid var(--card)}
.timeline{left:587px;top:872px;width:400px;height:4px;background:#e5e3de}
.dot{width:44px;height:44px;border-radius:50%;background:var(--yellow)}
.dot svg{position:absolute;left:15px;top:12px}
.year{width:80px;font-size:16px;color:#666}

/* what we do */
.what{left:8px;top:1062px;width:1185px;height:626px;background:var(--cream)}
.product{width:276px;height:200px}
.p-title{width:276px;font-size:18px;color:#5a5d61}
.p-text{width:276px;font-size:11px;line-height:18.5px;color:#7d7f82;font-weight:300}

/* health */
.health{left:8px;top:1688px;width:1185px;height:717px;background:linear-gradient(160deg,#4d4942 0%,#3f3c36 40%,#4b4536 65%,#3b382f 100%)}
.health-title{left:0;top:1775px;width:1200px;font-size:60px;color:#efeadc}
.b-title{font-size:19px;color:var(--yellow);white-space:nowrap}
.b-text{width:215px;font-size:12px;line-height:21px;color:#ece8dc}
.b-rule{width:26px;height:2px;background:#ece8dc}
.num{width:34px;height:34px;border-radius:50%;background:var(--yellow);color:#6b5a1a;font-size:13px;line-height:34px;text-align:center}
.olives{left:490px;top:2030px;width:220px;height:220px;border-radius:50%;background:radial-gradient(circle at 45% 50%,#9a1f2a 0%,#7a1520 40%,#d8d3c3 80%,#eee 100%)}

/* team */
.member{width:158px;height:158px;border-radius:50%}
.m-name{width:240px;font-size:18px;color:#5a5d61}
.m-rule{width:26px;height:2px;background:#5a5d61}

/* footer */
.footer{left:0;top:2901px;width:1200px;height:496px;background:var(--footer)}
.f-head{font-size:17px;color:var(--yellow)}
.f-rule{width:26px;height:2px;background:#d8d8d8}
.f-text{font-size:11px;line-height:18.5px;color:#b6b8bc;font-weight:300}
.email{left:613px;top:3102px;width:160px;height:40px;border:1px solid #555861;font-size:11px;color:#9a9ca0;padding:13px 18px;font-weight:300}
.check{left:613px;top:3157px;width:12px;height:12px;background:#fff}
.subscribe{left:613px;top:3197px;width:115px;height:30px;background:var(--yellow);color:#6b5a1a;font-size:9px;letter-spacing:1px;text-align:center;line-height:30px}
.social{width:30px;height:30px;border-radius:50%;background:var(--yellow)}
.copy{left:161px;top:3322px;font-size:11px;color:#fff;font-weight:300}
.copy b{color:var(--yellow);font-weight:300}
</style>
</head>
<body>

<header class="abs site-header">
  <div class="abs brand">BREVONIX</div>
  <ul class="abs nav">
    <li>HOME</li><li>ABOUT US</li><li>PRODUCTS</li><li>CSR</li><li>NEWS</li><li>CONTACT US</li>
  </ul>
</header>

<section class="abs hero" role="img" aria-label="Olive oil being poured from a bottle"></section>
<h1 class="abs hero-title serif center">About us</h1>
<div class="abs crumbs serif center">Home<span>/</span>About us</div>
<div class="abs badge" style="left:563px;top:382px"><i role="img" aria-label="Olive branch"></i></div>

<h2 class="abs section-title serif center" style="top:505px">Our Story</h2>
<div class="abs story-box"></div>
<div class="abs story-photo" role="img" aria-label="Glass jug of olive oil with black olives"></div>
<div class="abs story-card center">
  <h3 class="serif">High Quality</h3>
  <p>The oil is produced by using olive &amp; rapeseed and is commonly used in cooking, cosmetics, pharmaceuticals and is used throughout the world.</p>
</div>
<div class="abs card-tip"></div>
<div class="abs timeline"></div>
<div class="abs dot" style="left:606px;top:852px"><svg width="14" height="20" viewBox="0 0 14 20"><path d="M7 1C4 7 2 10 2 13a5 5 0 0 0 10 0c0-3-2-6-5-12z" fill="#6b5a1a"/></svg></div>
<div class="abs dot" style="left:686px;top:852px"><svg width="14" height="20" viewBox="0 0 14 20"><path d="M7 1C4 7 2 10 2 13a5 5 0 0 0 10 0c0-3-2-6-5-12z" fill="#6b5a1a"/></svg></div>
<div class="abs dot" style="left:765px;top:852px"><svg width="14" height="20" viewBox="0 0 14 20"><path d="M7 1C4 7 2 10 2 13a5 5 0 0 0 10 0c0-3-2-6-5-12z" fill="#6b5a1a"/></svg></div>
<div class="abs dot" style="left:846px;top:852px"><svg width="14" height="20" viewBox="0 0 14 20"><path d="M7 1C4 7 2 10 2 13a5 5 0 0 0 10 0c0-3-2-6-5-12z" fill="#6b5a1a"/></svg></div>
<div class="abs dot" style="left:925px;top:852px"><svg width="14" height="20" viewBox="0 0 14 20"><path d="M7 1C4 7 2 10 2 13a5 5 0 0 0 10 0c0-3-2-6-5-12z" fill="#6b5a1a"/></svg></div>
<div class="abs year center" style="left:588px;top:903px">1957</div>
<div class="abs year center" style="left:668px;top:903px">1962</div>
<div class="abs year center" style="left:747px;top:903px">1974</div>
<div class="abs year center" style="left:828px;top:903px">2006</div>
<div class="abs year center" style="left:907px;top:903px">2016</div>

<section class="abs what"></section>
<div class="abs badge" style="left:563px;top:1030px"><i role="img" aria-label="Olive branch"></i></div>
<h2 class="abs section-title serif center" style="top:1147px">What We Do</h2>
<div class="abs product" style="left:160px;top:1257px;background:linear-gradient(135deg,#c8261c,#e4452f 50%,#b8281c)" role="img" aria-label="Bowl of ketchup with fresh tomatoes"></div>
<div class="abs product" style="left:462px;top:1257px;background:radial-gradient(circle at 45% 55%,#f5ecc4 0%,#e9dca8 30%,#8a6a45 70%,#5d4632 100%)" role="img" aria-label="Bowl of mayonnaise with parsley"></div>
<div class="abs product" style="left:763px;top:1257px;background:radial-gradient(circle at 70% 65%,#e8702f 0%,#c9a774 35%,#5b2a26 65%,#222 100%)" role="img" aria-label="Bowls of lentils, chickpeas and beans"></div>
<div class="abs p-title serif center" style="left:160px;top:1481px">Lorem Ipsum</div>
<div class="abs p-title serif center" style="left:462px;top:1481px">Lorem Ipsum</div>
<div class="abs p-title serif center" style="left:763px;top:1481px;color:var(--gold)">Lorem Ipsum</div>
<p class="abs p-text center" style="left:160px;top:1523px">Lorem ipsum dolor sit amet, consectetur adipiscing elit, sed do eiusmod tempor incididunt ut labore et dolore magna aliqua. Ut enim ad minim.</p>
<p class="abs p-text center" style="left:462px;top:1523px">Lorem ipsum dolor sit amet, consectetur adipiscing elit, sed do eiusmod tempor incididunt ut labore et dolore magna aliqua. Ut enim ad minim.</p>
<p class="abs p-text center" style="left:763px;top:1523px">Lorem ipsum dolor sit amet, consectetur adipiscing elit, sed do eiusmod tempor incididunt ut labore et dolore magna aliqua. Ut enim ad minim.</p>

<section class="abs health" role="img" aria-label="Bottle of olive oil on a rustic table"></section>
<h2 class="abs health-title serif center">Health Benefits</h2>
<div class="abs olives" role="img" aria-label="Red olives with leaves"></div>

<div class="abs b-title serif" style="right:803px;top:1945px">Prevents Heart Attacks</div>
<div class="abs b-rule" style="left:366px;top:1978px"></div>
<div class="abs num" style="left:412px;top:1942px">1.</div>
<p class="abs b-text" style="left:182px;top:1993px;text-align:right">Lorem ipsum dolor sit amet, consectetur adipiscing elit, sed do eiusmod tempor.</p>

<div class="abs b-title serif" style="right:803px;top:2089px">Improves Your Memory</div>
<div class="abs b-rule" style="left:366px;top:2122px"></div>
<div class="abs num" style="left:412px;top:2086px">3.</div>
<p class="abs b-text" style="left:182px;top:2137px;text-align:right">Lorem ipsum dolor sit amet, consectetur adipiscing elit, sed do eiusmod tempor.</p>

<div class="abs b-title serif" style="right:803px;top:2234px">Helps Fight Cancer</div>
<div class="abs b-rule" style="left:366px;top:2267px"></div>
<div class="abs num" style="left:412px;top:2231px">5.</div>
<p class="abs b-text" style="left:182px;top:2282px;text-align:right">Lorem ipsum dolor sit amet, consectetur adipiscing elit, sed do eiusmod tempor.</p>

<div class="abs num" style="left:754px;top:1942px">2.</div>
<div class="abs b-title serif" style="left:802px;top:1945px">Reduces Cholesterol Levels</div>
<div class="abs b-rule" style="left:802px;top:1978px"></div>
<p class="abs b-text" style="left:802px;top:1993px">Lorem ipsum dolor sit amet, consectetur adipiscing elit, sed do eiusmod tempor.</p>

<div class="abs num" style="left:754px;top:2086px">4.</div>
<div class="abs b-title serif" style="left:802px;top:2089px">Helps Digestion</div>
<div class="abs b-rule" style="left:802px;top:2122px"></div>
<p class="abs b-text" style="left:802px;top:2137px">Lorem ipsum dolor sit amet, consectetur adipiscing elit, sed do eiusmod tempor.</p>

<div class="abs num" style="left:754px;top:2231px">6.</div>
<div class="abs b-title serif" style="left:802px;top:2234px">Prevents Blood Clotting</div>
<div class="abs b-rule" style="left:802px;top:2267px"></div>
<p class="abs b-text" style="left:802px;top:2282px">Lorem ipsum dolor sit amet, consectetur adipiscing elit, sed do eiusmod tempor.</p>

<h2 class="abs section-title serif center" style="top:2487px">Our Team</h2>
<div class="abs member" style="left:181px;top:2603px;background:linear-gradient(180deg,#8a8580,#b98a6e 55%,#2aa7c9 85%)" role="img" aria-label="Portrait of team member Adam Kerr"></div>
<div class="abs member" style="left:408px;top:2603px;background:linear-gradient(180deg,#7a6a60,#5a3a2a 40%,#d9b39a 60%,#6e7a8a)" role="img" aria-label="Portrait of team member Nina Hale"></div>
<div class="abs member" style="left:633px;top:2603px;background:linear-gradient(180deg,#d8d8d8,#5a4030 30%,#d9ae94 55%,#e9eaf0)" role="img" aria-label="Portrait of team member Mark Doyle"></div>
<div class="abs member" style="left:860px;top:2603px;background:linear-gradient(180deg,#e0ddd8,#8a4a2c 35%,#e2b29a 60%,#f2f0ee)" role="img" aria-label="Portrait of team member Vera Lind"></div>
<div class="abs m-name serif center" style="left:140px;top:2784px">Adam Kerr</div>
<div class="abs m-name serif center" style="left:367px;top:2784px">Nina Hale</div>
<div class="abs m-name serif center" style="left:592px;top:2784px">Mark Doyle</div>
<div class="abs m-name serif center" style="left:819px;top:2784px">Vera Lind</div>
<div class="abs m-rule" style="left:247px;top:2815px"></div>
<div class="abs m-rule" style="left:474px;top:2815px"></div>
<div class="abs m-rule" style="left:699px;top:2815px"></div>
<div class="abs m-rule" style="left:926px;top:2815px"></div>

<footer class="abs footer"></footer>
<div class="abs f-head serif" style="left:161px;top:3002px">About Us</div>
<div class="abs f-rule" style="left:161px;top:3030px"></div>
<p class="abs f-text" style="left:161px;top:3040px;width:195px">BREVONIX is a manufacturing and trading company in Wrocław , Poland We established longer and closer working relationships with our clients and supplier not only provide immediate and reliable service but to continually exceed expectations and goals.</p>

<div class="abs f-head serif" style="left:386px;top:3002px">Information</div>
<div class="abs f-rule" style="left:386px;top:3030px"></div>
<p class="abs f-text" style="left:386px;top:3040px">Home<br>Our Range<br>About Us<br>News<br>Contacts</p>

<div class="abs f-head serif" style="left:613px;top:3002px">Newsletter</div>
<div class="abs f-rule" style="left:613px;top:3030px"></div>
<p class="abs f-text" style="left:613px;top:3040px;width:200px">Stay up to date with all our recent products and promotions</p>
<div class="abs email">Your Email</div>
<div class="abs check"></div>
<p class="abs f-text" style="left:635px;top:3153px;width:185px;font-size:10px">I have read and agree to the terms &amp; conditions</p>
<div class="abs subscribe">SUBSCRIBE</div>

<div class="abs f-head serif" style="left:840px;top:3002px">Contact us</div>
<div class="abs f-rule" style="left:840px;top:3030px"></div>
<p class="abs f-text" style="left:840px;top:3040px;width:210px">Ul. Lipowa 18 /4a<br>50-111, Wrocław Polska</p>
<p class="abs f-text" style="left:840px;top:3096px">Phone: +48700123456<br>Email: info@brevonix.pl</p>
<div class="abs social" style="left:840px;top:3162px" role="img" aria-label="Social profile"></div>
<div class="abs social" style="left:874px;top:3162px" role="img" aria-label="Social profile"></div>

<p class="abs copy"><b>Brevonix</b> © 2020. All rights reserved.</p>

</body>
</html>
```